Urgent Cardiac Consult Request

We need a one page (1/2 pg size) order form for Urgent Cardiac Consults so that Emergency depts and walk -in clinics can fill this out and send forms with patient to our office. The page needs to have clear information, easy to read and to fill out. Our logo and address at the top and on the back side a map showing our location. I am sending a version that I have but the doctors want something different in the way of layout.
They want less information on them. At top - options for exam s: Excercise Stress Echo; Echocardiogram; Holter/Loop recorder (3day / 14 day/ other __); Concsult. Pt info in middle . Bottom : Indication s 1) Chest Pain/SOB 2: Palpatations 3) Other_____ Eyecatching, larger logo, etc Thanks

```html
<!DOCTYPE html>
<html lang="en">
<head>
<meta charset="utf-8">
<title>Rapid Cardiac Assessment – Order Form</title>
<link rel="stylesheet" href="https://fonts.googleapis.com/css2?family=Bebas+Neue&family=Roboto:ital,wght@0,400;0,500;0,700;0,900;1,400;1,500;1,700&display=swap">
<style>
  :root{
    --navy:#123b6e;
    --navy-deep:#0e3263;
    --red:#8e1620;
    --paper:#f1f2f4;
    --bar:#d5d7dc;
    --ink:#2a2d33;
    --rule:#3a3d44;
    --backdrop:#e6e6e8;
  }
  *{box-sizing:border-box;margin:0;padding:0}
  html,body{width:1180px;height:1200px;overflow:hidden}
  body{background:var(--backdrop);font-family:"Roboto",sans-serif;color:var(--ink);position:relative}

  .sheet{position:absolute;left:245px;top:184px;width:630px;height:826px;background:var(--paper);overflow:hidden}
  .header-art{position:absolute;left:0;top:0;width:630px;height:270px}
  .form-title{position:absolute;left:43px;top:32px;font-family:"Bebas Neue",sans-serif;font-size:32px;letter-spacing:.4px;color:#fff;line-height:1}

  .brand-badge{position:absolute;left:350px;top:28px;width:216px;height:216px;border-radius:50%;background:#fff;border:4px solid var(--navy);display:flex;align-items:center;justify-content:center;text-align:center}
  .brand-name{font-family:"Roboto",sans-serif;font-weight:700;font-size:21px;line-height:1.2;color:var(--navy);letter-spacing:.5px}

  .contact{position:absolute;left:42px;top:172px;font-size:14px;line-height:18px;color:var(--ink)}
  .contact .address{margin-top:7px}

  .section-bar{position:absolute;left:37px;width:558px;height:23px;background:var(--bar);padding-left:4px;font-weight:900;font-size:16px;letter-spacing:1.1px;color:var(--navy);line-height:23px}

  .field{position:absolute;display:flex;align-items:center;font-size:14px;color:var(--ink);white-space:nowrap;transform:translateY(-50%)}
  .box{display:inline-block;width:17px;height:17px;border:2px solid var(--navy);border-radius:3px;margin-right:9px;flex:none}
  .box.small{width:13px;height:13px;border-width:1.6px;border-radius:2px;margin-right:4px}
  .option-sub{font-style:italic;font-size:13px}
  .line{position:absolute;height:0;border-bottom:1.2px solid var(--rule)}

  .footer-band{position:absolute;left:0;top:782px;width:630px;height:44px;background:var(--navy-deep);color:#fff;text-align:center;font-style:italic}
  .footer-band .notice{font-weight:500;font-size:12.2px;margin-top:9px;letter-spacing:.1px}
  .footer-band .note{font-size:10.5px;margin-top:2px}
</style>
</head>
<body>
<main class="sheet">
  <svg class="header-art" viewBox="0 0 630 270" aria-hidden="true">
    <rect x="0" y="0" width="630" height="270" fill="var(--navy)"/>
    <path d="M0 122 Q170 88 365 92 L365 112 Q170 104 0 155 Z" fill="var(--red)"/>
    <path d="M0 155 Q170 104 365 112 L470 130 Q585 175 630 250 V270 H0 Z" fill="var(--paper)"/>
    <path d="M540 170 Q595 200 630 250" fill="none" stroke="var(--red)" stroke-width="3"/>
  </svg>

  <h1 class="form-title">Rapid Cardiac Assessment</h1>

  <div class="brand-badge">
    <span class="brand-name">LAKESHORE HEART<br>CENTRE</span>
  </div>

  <div class="contact">
    <p>Phone : 555-014-2200</p>
    <p>Fax : 555-014-2299</p>
    <p class="address">1180 Maple Avenue, Suite 300, Riverton</p>
    <p>Monday - Saturday : 8am-5pm</p>
  </div>

  <!-- Request for -->
  <h2 class="section-bar" style="top:272px">REQUEST FOR</h2>
  <div class="field" style="left:37px;top:318px"><span class="box"></span>Stress Echo/Test</div>
  <div class="field" style="left:247px;top:318px"><span class="box"></span>EKG</div>
  <div class="field" style="left:382px;top:318px"><span class="box"></span>Holter Monitor</div>
  <div class="field option-sub" style="left:410px;top:339px"><span class="box small"></span>24 - 72 hrs</div>
  <div class="field option-sub" style="left:492px;top:339px"><span class="box small"></span>7 - 14 days</div>
  <div class="field" style="left:37px;top:352px"><span class="box"></span>Echocardiogram</div>
  <div class="field" style="left:37px;top:383px"><span class="box"></span>Cardiology Consult</div>

  <!-- Indications -->
  <h2 class="section-bar" style="top:414px">INDICATIONS</h2>
  <div class="field" style="left:37px;top:464px"><span class="box"></span>Chest Pain/SOB</div>
  <div class="field" style="left:191px;top:464px"><span class="box"></span>Palpatations</div>
  <div class="field" style="left:325px;top:464px"><span class="box"></span>Other</div>
  <span class="line" style="left:396px;width:199px;top:469px"></span>

  <!-- Patient information -->
  <h2 class="section-bar" style="top:493px">PATIENT INFORMATION</h2>
  <div class="field" style="left:39px;top:540px">Full Name:</div>
  <span class="line" style="left:116px;width:479px;top:545px"></span>
  <div class="field" style="left:39px;top:574px">Date of Birth:</div>
  <span class="line" style="left:134px;width:261px;top:578px"></span>
  <div class="field" style="left:400px;top:575px">Gender</div>
  <div class="field" style="left:457px;top:575px"><span class="box"></span>Male</div>
  <div class="field" style="left:525px;top:575px"><span class="box"></span>Female</div>
  <div class="field" style="left:39px;top:605px">Health Card#:</div>
  <span class="line" style="left:137px;width:200px;top:610px"></span>
  <div class="field" style="left:346px;top:605px">Phone:</div>
  <span class="line" style="left:395px;width:200px;top:610px"></span>

  <!-- Physician information -->
  <h2 class="section-bar" style="top:633px">PHYSICIAN INFORMATION</h2>
  <div class="field" style="left:38px;top:681px">Physician Name:</div>
  <span class="line" style="left:153px;width:283px;top:686px"></span>
  <div class="field" style="left:442px;top:681px">Billing #:</div>
  <span class="line" style="left:501px;width:94px;top:686px"></span>
  <div class="field" style="left:38px;top:713px">Phone:</div>
  <span class="line" style="left:89px;width:233px;top:718px"></span>
  <div class="field" style="left:328px;top:713px">Fax:</div>
  <span class="line" style="left:360px;width:235px;top:718px"></span>
  <div class="field" style="left:38px;top:747px">Ordering Physician Signature:</div>
  <span class="line" style="left:235px;width:221px;top:752px"></span>
  <div class="field" style="left:462px;top:748px">Date:</div>
  <span class="line" style="left:501px;width:94px;top:752px"></span>

  <footer class="footer-band">
    <p class="notice">PLEASE PROVIDE A COMPLETE LIST OF MEDICATIONS AT TIME OF TESTING AND/OR CONSULTATION.</p>
    <p class="note">All abnormal test results will be followed by a cardiology consult unless otherwise requested</p>
  </footer>
</main>
</body>
</html>
```